Student Podcast Cover Art

This project is for cover art for my podcast. I prefer if both the binders and the backpack are in the photo. I need text over laid on the top left of the image with the words "Hallway Echoes". I think the font should in white, but you are free to change it to a different color. Not sure on the font, but needs to easy to read and eye catching (maybe add effects). I also need the colors of the picture to pop. I attached the image that is to be edited as well as my rough edit of the ideas that I envisioned. Thanks

Target Market(s)

Students (University, college, high school)

Font styles to use
Sans Serif
Script

Colors

Designer to choose colors to be used in the design.

Requirements
Must have
• add text "Hallway Echoes". Picture must be square in shape and 3000 by 3000 pixels. Picture has to be straight (the ground and wall).

```html
<!DOCTYPE html>
<html lang="en">
<head>
<meta charset="utf-8">
<title>Hallway Echoes — Podcast Cover</title>
<link rel="stylesheet" href="https://fonts.googleapis.com/css2?family=Abril+Fatface&display=swap">
<style>
  :root {
    --brick-light: #c07a62;
    --brick-mid: #b06a54;
    --brick-dark: #9c5c48;
    --pavement-light: #9a958f;
    --pavement-dark: #7d7873;
    --shirt-blue: #a9c2d8;
    --denim-blue: #34508a;
    --gear-grey: #5c6170;
    --title-yellow: #fff314;
    --title-white: #ffffff;
    --frame-white: #ffffff;
  }
  html, body {
    margin: 0;
    padding: 0;
    width: 1200px;
    height: 1200px;
    overflow: hidden;
    background: #ffffff;
  }
  .cover {
    position: relative;
    width: 1200px;
    height: 1200px;
  }
  .cover-art {
    display: block;
    width: 1200px;
    height: 1200px;
  }
  .title-text {
    font-family: "Abril Fatface", "Georgia", serif;
  }
  .title-top { fill: var(--title-yellow); }
  .title-bottom { fill: var(--title-white); }
  .title-reflection { fill: var(--title-white); opacity: 0.22; }
  .inner-frame {
    fill: none;
    stroke: var(--frame-white);
    stroke-width: 5;
  }
</style>
</head>
<body>
<main class="cover">
  <svg class="cover-art" viewBox="0 0 1200 1200" xmlns="http://www.w3.org/2000/svg">
    <defs>
      <linearGradient id="wallTone" x1="0" y1="0" x2="0" y2="1">
        <stop offset="0" stop-color="var(--brick-light)"/>
        <stop offset="0.5" stop-color="var(--brick-mid)"/>
        <stop offset="1" stop-color="var(--brick-dark)"/>
      </linearGradient>
      <linearGradient id="groundTone" x1="0" y1="0" x2="0" y2="1">
        <stop offset="0" stop-color="var(--pavement-light)"/>
        <stop offset="1" stop-color="var(--pavement-dark)"/>
      </linearGradient>
      <linearGradient id="subjectTone" x1="0" y1="0" x2="0" y2="1">
        <stop offset="0" stop-color="var(--brick-mid)" stop-opacity="0"/>
        <stop offset="0.25" stop-color="var(--shirt-blue)" stop-opacity="0.85"/>
        <stop offset="0.6" stop-color="var(--denim-blue)" stop-opacity="0.85"/>
        <stop offset="1" stop-color="var(--gear-grey)" stop-opacity="0.7"/>
      </linearGradient>
    </defs>

    <g class="cover-photo" role="img" aria-label="Photo of a smiling student sitting on pavement against a red brick wall, holding a coffee cup and an open notebook, with a stack of binders on the left and a grey backpack on the right">
      <rect class="photo-wall" x="0" y="0" width="1200" height="940" fill="url(#wallTone)"/>
      <rect class="photo-ground" x="0" y="940" width="1200" height="260" fill="url(#groundTone)"/>
      <rect class="photo-subject" x="156" y="457" width="886" height="708" rx="40" fill="url(#subjectTone)"/>
    </g>

    <rect class="inner-frame" x="29" y="29" width="1142" height="1142"/>

    <g class="podcast-title">
      <text class="title-text title-top" x="156" y="250" font-size="190" textLength="902" lengthAdjust="spacingAndGlyphs">HALLWAY</text>
      <text class="title-text title-bottom" x="156" y="382" font-size="140" textLength="912" lengthAdjust="spacingAndGlyphs">ECHOES</text>
      <text class="title-text title-reflection" x="156" y="-390" font-size="140" textLength="912" lengthAdjust="spacingAndGlyphs" transform="scale(1,-1)" aria-hidden="true">ECHOES</text>
    </g>
  </svg>
</main>
</body>
</html>
```